Endocrinologist needs new stationery

I have a logo from MarkForge and now need stationery with the new logo.

Address: Suite 4, 282 Falcon Street, Richmond, VIC 3121
Phone: 03 9417 2253
Fax: 03 9417 2255
Website: www.drmaylacorwen.com.au
Email: admin@drmaylacorwen.com.au

```html
<!DOCTYPE html>
<html lang="en">
<head>
<meta charset="utf-8">
<title>Dr Mayla Corwen – Stationery</title>
<link rel="stylesheet" href="https://fonts.googleapis.com/css2?family=Mulish:wght@300;400&display=swap">
<style>
  :root {
    --backdrop: #707070;
    --paper: #f3f3f3;
    --paper-white: #fbfbfb;
    --card-light: #ececeb;
    --brand-blue: #356b99;
    --brand-blue-deep: #2f5f89;
    --contact-plum: #6b3448;
    --faint-name: #e1e1e1;
    --shadow: rgba(0,0,0,0.28);
  }
  * { box-sizing: border-box; margin: 0; padding: 0; }
  html, body { width: 1200px; height: 1000px; overflow: hidden; }
  body {
    background: var(--backdrop);
    font-family: "Mulish", sans-serif;
    position: relative;
  }
  .sheet { position: absolute; overflow: hidden; box-shadow: 5px 6px 0 var(--shadow); }

  .brand-name {
    font-family: "Mulish", sans-serif;
    font-weight: 400;
    color: var(--brand-blue);
    line-height: 1;
    white-space: nowrap;
  }
  .contact {
    font-family: "Mulish", sans-serif;
    font-style: normal;
    font-weight: 400;
    color: var(--contact-plum);
    text-align: center;
    line-height: 1.3;
    white-space: nowrap;
  }
  .faint-name {
    position: absolute;
    font-family: "Mulish", sans-serif;
    font-weight: 300;
    color: var(--faint-name);
    line-height: 0.95;
    white-space: nowrap;
  }

  /* Letterhead */
  .letterhead { left: 560px; top: 124px; width: 582px; height: 814px; background: var(--paper); }
  .letterhead .brand-name { position: absolute; left: 40px; top: 44px; font-size: 19px; }
  .letterhead .contact { position: absolute; right: 50px; top: 42px; font-size: 9.5px; }
  .letterhead .faint-name { left: 6px; top: 548px; font-size: 100px; }
  .letterhead .faint-name span { display: block; padding-left: 150px; }

  /* Envelope */
  .envelope { left: 54px; top: 236px; width: 594px; height: 380px; background: var(--paper-white); }
  .envelope .flap { position: absolute; left: 0; top: 0; width: 100%; height: 92px; }
  .envelope .faint-name { left: 14px; top: 130px; font-size: 96px; }
  .envelope .faint-name span { display: block; padding-left: 140px; }

  /* Business cards */
  .card { width: 277px; height: 155px; }
  .card-back { left: 58px; top: 656px; background: var(--brand-blue); }
  .card-back .faint-name { color: var(--brand-blue-deep); left: 18px; top: 20px; font-size: 46px; }
  .card-back .faint-name span { display: block; padding-left: 60px; }
  .card-front { left: 232px; top: 780px; background: var(--card-light); }
  .card-front .brand-name { position: absolute; left: 0; right: 0; top: 56px; text-align: center; font-size: 19px; }
  .card-front .contact { position: absolute; left: 0; right: 0; top: 100px; font-size: 8.6px; }
</style>
</head>
<body>

  <section class="sheet card card-back" aria-label="Business card back">
    <p class="faint-name">Dr Mayla<span>Corwen</span></p>
  </section>

  <section class="sheet card card-front" aria-label="Business card front">
    <p class="brand-name">Dr Mayla Corwen</p>
    <address class="contact">
      Suite 4, 282 Falcon Street, Richmond, VIC 3121<br>
      03 9417 2253 • admin@drmaylacorwen.com.au<br>
      www.drmaylacorwen.com.au
    </address>
  </section>

  <section class="sheet letterhead" aria-label="Letterhead">
    <p class="brand-name">Dr Mayla Corwen</p>
    <address class="contact">
      Suite 4, 282 Falcon Street, Richmond, VIC 3121<br>
      03 9417 2253 • admin@drmaylacorwen.com.au<br>
      www.drmaylacorwen.com.au
    </address>
    <p class="faint-name">Dr Mayla<span>Corwen</span></p>
  </section>

  <section class="sheet envelope" aria-label="Envelope">
    <svg class="flap" viewBox="0 0 594 92" preserveAspectRatio="none" aria-hidden="true">
      <polygon points="0,30 30,24 594,0 594,70 0,92" fill="var(--brand-blue)"/>
    </svg>
    <p class="faint-name">Dr Mayla<span>Corwen</span></p>
  </section>

</body>
</html>
```